New Zealand Kestrel Bridgeway Flyer

A 2 sided DL size flyer. (Approx 20cm long by 10cm wide)
That has logo and blurb about company on front. On back details of Kestrel bridgeway package, trademark, contact details and license numbers.
We feel we need to see the text on the flyer design and then make some changes so there will be some back and forth about written content. There may be a reduction in the amount of text we want for the blurb about the company but the rest is mandatory.
Our logo is blue and green, we do not want a white flyer with black text as feel this looks homemade so we need your suggestions about what colour the text and flyer could be.
We want the flyer to look clean and modern. It will go on a stand at an immigration fair and will be sent in the post and via email to clients. We will need posters at a later stage.
Migrants
It Company

```html
<!DOCTYPE html>
<html lang="en">
<head>
<meta charset="utf-8">
<title>New Zealand Kestrel Bridgeway – DL Flyer</title>
<link rel="stylesheet" href="https://fonts.googleapis.com/css2?family=Arimo:ital,wght@0,400;0,700;1,400&display=swap">
<style>
  :root {
    --page-bg: #e9ecec;
    --paper: #eef5fb;
    --brand-blue: #1565c0;
    --brand-green: #3aaa35;
    --ink: #123a63;
    --ink-accent: #1565c0;
    --badge: #a9b57a;
  }
  * { box-sizing: border-box; margin: 0; padding: 0; }
  html, body { width: 1200px; height: 1000px; overflow: hidden; }
  body {
    background: var(--page-bg);
    font-family: "Arimo", Arial, sans-serif;
    color: var(--ink);
    display: flex;
    align-items: center;
    justify-content: center;
    gap: 60px;
  }
  .flyer {
    position: relative;
    width: 400px;
    height: 800px;
    background: var(--paper);
    box-shadow: 0 4px 18px rgba(0,0,0,.12);
    overflow: hidden;
  }
  .band { position: absolute; left: 0; right: 0; height: 14px; }
  .band--blue { background: var(--brand-blue); }
  .band--green { background: var(--brand-green); }

  /* Front */
  .front .band--blue { bottom: 14px; }
  .front .band--green { bottom: 0; }
  .brand {
    display: flex; align-items: center; justify-content: center;
    gap: 12px; margin: 44px 0 34px;
  }
  .brand__dot { width: 40px; height: 40px; border-radius: 50%; background: var(--brand-green); }
  .brand__name {
    color: var(--brand-blue); font-weight: 700; font-size: 22px; line-height: 1.1;
  }
  .front__content { padding: 0 30px; }
  .front__headline {
    text-align: center; font-weight: 700; font-size: 14px; line-height: 1.6;
    margin-bottom: 30px; color: var(--ink-accent); white-space: nowrap;
  }
  .front__blurb { font-size: 14px; line-height: 1.6; margin-bottom: 30px; }
  .front__blurb strong { display: block; font-size: 15px; color: var(--ink-accent); }
  .front__quote { font-style: italic; font-size: 14px; line-height: 1.6; text-align: center; margin-bottom: 34px; }
  .front__skills { font-size: 14px; line-height: 1.7; padding-left: 12px; }

  /* Back */
  .back .band--blue { top: 0; }
  .back .band--green { top: 14px; }
  .back__content { padding: 56px 30px 0; font-size: 12.5px; line-height: 1.5; }
  .back__title { text-align: center; font-size: 16px; font-weight: 700; margin-bottom: 8px; color: var(--ink-accent); }
  .back__intro { text-align: center; margin-bottom: 12px; }
  .benefits { list-style: none; margin-bottom: 14px; }
  .benefits li { padding-left: 12px; position: relative; margin-bottom: 6px; }
  .benefits li::before { content: "•"; position: absolute; left: 0; color: var(--brand-green); }
  .package { display: flex; gap: 12px; align-items: flex-start; margin-bottom: 14px; }
  .package__badge { flex: 0 0 58px; height: 58px; border-radius: 50%; background: var(--badge); margin-top: 6px; }
  .back__cta { font-weight: 700; margin-bottom: 10px; color: var(--ink-accent); }
  .licences { font-weight: 700; line-height: 1.6; }
</style>
</head>
<body>

  <section class="flyer front">
    <header class="brand">
      <span class="brand__dot"></span>
      <span class="brand__name">New Zealand<br>Kestrel Bridgeway</span>
    </header>
    <div class="front__content">
      <p class="front__headline">Friendly &amp; helpful Licensed Immigration Advisers<br>We facilitate fast and problem free visas</p>
      <p class="front__blurb">New Zealand Kestrel Bridgeway is a family business; headed by two sisters – Mara and Ines Calloway. Originally from the UK they migrated to New Zealand over ten years ago, so understand how it feels to move to a new country &amp; go through the visa process. Ines &amp; Mara are passionate about what New Zealand has to offer and enjoy the chance to help people make their home here. They work across all types of visa applications – <strong>to live, work or study.</strong></p>
      <p class="front__quote">“Working closely with you to meet your immigration goals, we help and guide you at every stage.”</p>
      <p class="front__skills">Trained and qualified, they have specialist knowledge of the immigration system. Able to work to urgent timeframes or with clients who have character or health issues.</p>
    </div>
    <div class="band band--blue"></div>
    <div class="band band--green"></div>
  </section>

  <section class="flyer back">
    <div class="band band--blue"></div>
    <div class="band band--green"></div>
    <div class="back__content">
      <h2 class="back__title">Kestrel Bridgeway Package</h2>
      <p class="back__intro">Set yourself on a clear pathway from your first student visa to permanent residency with our comprehensive immigration package.</p>
      <p class="back__intro">Connect with licensed advisers who walk alongside you in your New Zealand journey, helping to make the most of your time and money.</p>
      <ul class="benefits">
        <li>Confirmed, discounted rates for ongoing visas once your study is completed</li>
        <li>A one on one session with a licensed adviser to plan how to maximise your studies &amp; work opportunities to achieve residency faster</li>
        <li>Attendance at an immigration seminar</li>
        <li>Vital updates on immigration policy changes and how they impact on you</li>
        <li>Access to immediate advice from someone who knows your situation if things go wrong</li>
      </ul>
      <div class="package">
        <p>The Kestrel Bridgeway Package includes 3 visa applications, which covers Post Study Work Visa – Open, Post Study Work Visa – Employer Assisted Visa or Work to Residence (this includes employer support) and a Resident Visa via Skilled Migrant Category or Work to Residence (components for latter). Payment options available.</p>
        <span class="package__badge" role="img" aria-label="Licensing authority badge"></span>
      </div>
      <p class="back__cta">Contact us to plan your route to residency.</p>
      <p class="licences">Licence Number 209904417<br>Licence Number 209905532<br>hello@kestrelbridgeway.example</p>
    </div>
  </section>

</body>
</html>
```